Bussines Card - RM EDIFICACIONES, S.A.

We need a design for a business card.
I want it to look professional, but not old fashion.
We are like "young people', somehow i want it to look fresh, new, different, but still serious and professional.
I could use, a non typical design. (I mean, not just rectangular design).

The company Name is " RM EDIFICACIONES, S.A. " we are Panamenian company (spanish language) dedicated to construction and civil engeniering.

The company logo is attached, i use it with white background. Im not sure trying different one, could try.

```html
<!DOCTYPE html>
<html lang="es">
<head>
<meta charset="utf-8">
<title>RM Edificaciones – Tarjeta de presentación</title>
<link rel="stylesheet" href="https://fonts.googleapis.com/css2?family=Fira+Sans+Condensed:wght@400;600;700&display=swap">
<style>
  :root {
    --backdrop: #1c1c1d;
    --card-white: #ffffff;
    --card-grey-light: #6a6a6d;
    --card-grey-dark: #3f3f42;
    --ink: #3a3a3a;
    --ink-soft: #6b6b6b;
    --rule: #b5b5b5;
    --mark: #4a4a4c;
    --on-dark: #ffffff;
  }
  * { box-sizing: border-box; margin: 0; padding: 0; }
  html, body { width: 1200px; height: 675px; overflow: hidden; }
  body {
    background: var(--backdrop);
    font-family: "Fira Sans Condensed", "Arial Narrow", sans-serif;
    position: relative;
  }
  .card {
    position: absolute;
    top: 195px;
    width: 500px;
    height: 286px;
    border-radius: 2px;
  }
  /* Front: personal card */
  .card--front { left: 75px; background: var(--card-white); color: var(--ink); }
  .brand-block { position: absolute; left: 42px; top: 36px; display: flex; align-items: center; gap: 10px; }
  .brand-square { width: 58px; height: 58px; background: var(--mark); }
  .brand-name { font-weight: 700; font-size: 13px; letter-spacing: 1px; color: var(--mark); }
  .person { position: absolute; left: 42px; top: 104px; }
  .person__name { font-weight: 700; font-size: 17px; letter-spacing: .5px; color: var(--mark); }
  .person__role { font-weight: 600; font-size: 9px; letter-spacing: .8px; color: var(--ink-soft); margin-top: 1px; }
  .contact {
    position: absolute; left: 215px; top: 148px;
    border-left: 1px solid var(--rule);
    padding-left: 14px;
    font-size: 10.5px; line-height: 1.45; letter-spacing: .4px; color: var(--ink-soft);
  }
  .contact__address { margin-bottom: 8px; text-transform: uppercase; }
  .contact__row { display: flex; align-items: center; gap: 8px; text-transform: uppercase; }
  .contact__row svg { width: 10px; height: 10px; fill: var(--ink-soft); flex: none; }

  /* Back: company card */
  .card--back {
    left: 625px;
    background: linear-gradient(135deg, var(--card-grey-light) 0%, var(--card-grey-dark) 100%);
    color: var(--on-dark);
  }
  .back-square { position: absolute; left: 195px; top: 50px; width: 110px; height: 110px; background: var(--on-dark); }
  .back-name {
    position: absolute; left: 0; right: 0; top: 190px; text-align: center;
    font-weight: 600; font-size: 31px; letter-spacing: 3px;
  }
</style>
</head>
<body>
  <section class="card card--front" aria-label="Tarjeta, cara personal">
    <div class="brand-block">
      <div class="brand-square"></div>
      <span class="brand-name">RM EDIFICACIONES</span>
    </div>
    <div class="person">
      <p class="person__name">CARLOS MÉNDEZ</p>
      <p class="person__role">PRESIDENT &amp; CEO</p>
    </div>
    <div class="contact">
      <p class="contact__address">Calle 50, Bella Vista, Plaza Coral,<br>2do piso local 4</p>
      <p class="contact__row">
        <svg viewBox="0 0 10 10"><path d="M2 1h2l1 2.5-1.2.8a5 5 0 0 0 2 2l.8-1.2L9 6v2a1 1 0 0 1-1 1A7 7 0 0 1 1 2a1 1 0 0 1 1-1z"/></svg>
        395-4417
      </p>
      <p class="contact__row">
        <svg viewBox="0 0 10 10"><path d="M3 0h4a1 1 0 0 1 1 1v8a1 1 0 0 1-1 1H3a1 1 0 0 1-1-1V1a1 1 0 0 1 1-1zm0 1.5v6h4v-6z"/></svg>
        507-614-2290
      </p>
      <p class="contact__row">
        <svg viewBox="0 0 10 10"><path d="M0 2h10v6H0zm1 1v.3l4 2.4 4-2.4V3z"/></svg>
        carlos@rmedifica.com
      </p>
      <p class="contact__row">
        <svg viewBox="0 0 10 10"><path d="M5 0a5 5 0 1 0 0 10A5 5 0 0 0 5 0zm0 1c.6 0 1.3 1.3 1.5 3.5h-3C3.7 2.3 4.4 1 5 1zM1 5.5h1.5c.1 1.3.3 2.3.7 3A4 4 0 0 1 1 5.5zm0-1A4 4 0 0 1 3.2 1.5c-.4.8-.6 1.8-.7 3zm4 4.5c-.6 0-1.3-1.3-1.5-3.5h3C6.3 7.7 5.6 9 5 9zm1.8-.5c.4-.7.6-1.7.7-3H9a4 4 0 0 1-2.2 3zm.7-4c-.1-1.2-.3-2.2-.7-3A4 4 0 0 1 9 4.5z"/></svg>
        www.rmedifica.com
      </p>
    </div>
  </section>

  <section class="card card--back" aria-label="Tarjeta, cara de empresa">
    <div class="back-square"></div>
    <p class="back-name">RM EDIFICACIONES</p>
  </section>
</body>
</html>
```